Business Card Design for Kidvale (Hires out childrens play areas)

Looking to have a business card designed for a company we just bought. The company rents out childrens play areas.

I have uploaded a couple of examples of the kind of business card style I like. Here are two more examples:

https://quorvastudio.nz/project/bright-romp-branding/
https://imgvaultcdn.com/design_img/8841052/302917/302917_5518203_8841052_b73e19a2_image.jpg

I think a white card will be best due to all the colours in the logo.

Size we require: 3.75" x 2.25" (horizontally orientated) with a 0.125" bleed

Uploaded is two versions of our logo.

Details for the card:
1. My name: Liam Verster
2. Title: Managing Director
3. Phone no: 021 563 417
4. Email: liam@kidvale.co.nz
5. URL: www.kidvale.co.nz
6. Address:
PO Box 318625
Fernlea, Auckland

Let me know if you need anything else.

Target Market(s)

Hospitals, doctors surgeries, bed shops, etc.

Contact Information for Business Card

Details for the card:
1. My name: Liam Verster
3. Phone no: 021 563 417
5. URL: www.kidvale.co.nz
6. Address:
PO Box 318625
Fernlea, Auckland

Requirements
Should not have
• Not too busy.

```html
<!DOCTYPE html>
<html lang="en">
<head>
<meta charset="utf-8">
<title>Kidvale — Business Card</title>
<link rel="stylesheet" href="https://fonts.googleapis.com/css2?family=Montserrat:wght@400;500;700;800&family=Titan+One&display=swap">
<style>
  :root {
    --backdrop: #b7c3ca;
    --card-white: #f4f3f1;
    --brand-purple: #6e2f92;
    --ink: #3a3a3c;
    --link-blue: #1f5fa8;
    --label-green: #3aa541;
    --label-orange: #ee8a1c;
    --edge-blue: #1f5fa8;
  }
  * { box-sizing: border-box; margin: 0; padding: 0; }
  html, body { width: 1200px; height: 1023px; overflow: hidden; }
  body {
    background: var(--backdrop);
    font-family: "Montserrat", sans-serif;
    color: var(--ink);
    display: flex;
    flex-direction: column;
    align-items: center;
    justify-content: center;
    gap: 64px;
  }
  .card {
    width: 600px;
    height: 360px;
    position: relative;
    border-bottom: 4px solid var(--edge-blue);
    box-shadow: 0 10px 24px rgba(40, 55, 70, 0.22);
  }
  .card--front {
    background: var(--brand-purple);
    display: flex;
    align-items: center;
    justify-content: center;
  }
  .brand {
    display: flex;
    align-items: center;
    gap: 16px;
    font-family: "Montserrat", sans-serif;
    font-weight: 800;
  }
  .brand__dot { border-radius: 50%; flex: none; }
  .card--front .brand { font-size: 72px; color: #ffffff; }
  .card--front .brand__dot { width: 44px; height: 44px; background: #ffffff; }

  .card--back { background: var(--card-white); }
  .holder {
    position: absolute;
    left: 58px;
    top: 54px;
  }
  .holder__name {
    font-family: "Titan One", sans-serif;
    font-size: 30px;
    color: var(--brand-purple);
    text-transform: uppercase;
    letter-spacing: 0.5px;
    line-height: 1;
  }
  .holder__title { font-size: 13px; margin-top: 6px; }
  .address {
    position: absolute;
    left: 58px;
    top: 140px;
    font-size: 14px;
    line-height: 1.45;
  }
  .website {
    position: absolute;
    left: 58px;
    top: 200px;
    font-size: 14px;
    color: var(--link-blue);
  }
  .website b { font-weight: 700; }
  .contact {
    position: absolute;
    left: 300px;
    top: 220px;
    font-size: 14px;
    line-height: 1.3;
  }
  .contact__label { font-weight: 700; font-size: 13px; }
  .contact__label--mobile { color: var(--label-green); }
  .contact__label--email { color: var(--label-orange); margin-top: 10px; }
  .card--back .brand {
    position: absolute;
    right: 40px;
    top: 226px;
    font-size: 24px;
    color: var(--brand-purple);
    gap: 8px;
  }
  .card--back .brand__dot { width: 18px; height: 18px; background: var(--brand-purple); }
</style>
</head>
<body>
  <section class="card card--front" aria-label="Card front">
    <div class="brand"><span class="brand__dot"></span><span>Kidvale</span></div>
  </section>

  <section class="card card--back" aria-label="Card back">
    <div class="holder">
      <h1 class="holder__name">Liam Verster</h1>
      <p class="holder__title">Managing Director</p>
    </div>
    <p class="address">PO Box 318625<br>Fernlea, Auckland</p>
    <p class="website">www.<b>kidvale</b>.co.nz</p>
    <div class="contact">
      <p class="contact__label contact__label--mobile">mobile</p>
      <p>021 563 417</p>
      <p class="contact__label contact__label--email">email</p>
      <p>liam@kidvale.co.nz</p>
    </div>
    <div class="brand"><span class="brand__dot"></span><span>Kidvale</span></div>
  </section>
</body>
</html>
```